Redesign of key pages of website

We have a website in development: (You can see the test version here: https://staging.pipwoof.ai) We want a redesign of a) the home page, b) the set up screens (all four steps), c) the account home page, and the chat page (all four linked below). It needs to look amazing in both desktop and mobile. Also, the chat page needs to have a few different versions to give people a choice between them.

Four areas:
1) Home page: https://staging.pipwoof.ai/
2) Account pages: https://staging.pipwoof.ai/account/chatsettings.php?step=1
3) Account home page (you'll need to set up an account which is free): https://staging.pipwoof.ai/account/summary.php
4) Chat page: https://staging.pipwoof.ai/chat.php?id=375

Also to clarify re: code, I don't need any of the interaction/behavior code. I just need the basic HTML and stylesheets so I can integrate that into the existing website.

Please feel free to pass by early versions to me or if you have any clarifications, let me know!

Industry/Entity Type

small businesses

Coding

Coded - Design and coding required

Number of Pages Required

5+ page

Font styles to use
Other font styles liked:
• keep the current font.

Requirements
Must have
• All the same elements/functionality on the current site. Just want a redesign. Also keep the dog visual. Also must work great in mobile and desktop and be really fun and modern and easy.
Nice to have
• Also in the setup pages, need a much better form of navigation (currently just have four circles.)

```html
<!DOCTYPE html>
<html lang="en">
<head>
<meta charset="utf-8">
<title>pipwoof! — Let Pip Handle Your Leads</title>
<link href="https://fonts.googleapis.com/css2?family=Lexend:wght@300;400;500;700&family=Josefin+Sans:wght@400;600&display=swap" rel="stylesheet">
<style>
  :root{
    --mint:#d8f3ef;
    --teal:#0ba896;
    --teal-line:#7fd8cc;
    --pink:#ff6b6b;
    --pink-soft:#ffc7ca;
    --blue:#3b7ef6;
    --periwinkle:#aab6fb;
    --ink:#333336;
    --muted:#6b6b73;
    --white:#ffffff;
  }
  *{box-sizing:border-box;margin:0;padding:0}
  html,body{width:1200px;height:3008px;overflow:hidden;background:var(--white)}
  body{position:relative;font-family:"Josefin Sans",sans-serif;color:var(--ink)}
  .abs{position:absolute}
  .backdrop{position:absolute;left:0;top:0}
  .brand{font-family:"Lexend",sans-serif;font-weight:700;color:var(--ink);letter-spacing:-1px}
  .btn{position:absolute;display:flex;align-items:center;justify-content:space-between;padding:0 18px 0 28px;border-radius:5px;font-family:"Lexend",sans-serif;font-size:9px;font-weight:700;letter-spacing:2px;text-transform:uppercase;color:var(--white);text-decoration:none}
  .btn svg{width:14px;height:14px}
  .btn--blue{background:var(--blue)}
  .btn--pink{background:var(--pink)}
  .btn--teal{background:var(--teal)}
  .btn--white{background:var(--white);color:var(--ink)}
  .illustration{position:absolute;border-radius:45% 45% 30% 30%;background:linear-gradient(135deg,var(--periwinkle) 0%,var(--periwinkle) 50%,var(--blue) 51%,var(--blue) 100%)}
  .h-display{font-family:"Lexend",sans-serif;font-weight:400;color:var(--ink);line-height:1.08;letter-spacing:-1px}
  .underlined{position:relative;display:inline-block}
  .underlined::after{content:"";position:absolute;left:-2%;right:-6%;bottom:-2px;height:6px;border-radius:3px;background:var(--blue);transform:rotate(-0.6deg)}
  .underlined--pink::after{background:var(--pink)}
  .body-copy{font-size:14px;line-height:29px;color:var(--ink);letter-spacing:.3px}
  .icon-dot{position:absolute;width:55px;height:55px;border-radius:50%;display:flex;align-items:center;justify-content:center}
  .icon-dot--pink{background:var(--pink-soft)}
  .icon-dot--mint{background:var(--mint)}
  .icon-dot svg{width:26px;height:26px}
  .bubble-text{position:absolute;left:776px;top:240px;width:230px;text-align:center;font-family:"Lexend",sans-serif;font-weight:300;font-size:19px;line-height:28px}
  /* chat card */
  .chat-card{position:absolute;left:250px;top:881px;width:262px;height:194px;background:var(--white);border-radius:10px;border-left:6px solid var(--pink);border-bottom:6px solid var(--pink);box-shadow:0 6px 18px rgba(0,0,0,.06);font-family:"Lexend",sans-serif}
  .chat-card .avatar{position:absolute;left:16px;top:14px;width:40px;height:40px;border-radius:50%;border:2px solid #f3a27a}
  .chat-card .name{position:absolute;left:70px;top:16px;font-size:12px;font-weight:500}
  .chat-card .role{position:absolute;left:70px;top:32px;font-size:8px;color:var(--muted)}
  .chat-card .socials{position:absolute;left:72px;top:50px;display:flex;gap:12px}
  .chat-card .socials span{width:13px;height:13px;border-radius:50%;background:#2b2b30}
  .chat-card .bot{position:absolute;left:18px;top:88px;width:42px;height:42px;border-radius:50%;background:var(--periwinkle)}
  .chat-card .msg{position:absolute;left:78px;top:96px;font-size:9px;line-height:14px;color:var(--ink)}
  .chat-card .input{position:absolute;left:10px;right:10px;bottom:10px;height:22px;border-radius:4px;background:#f4f6f8;font-size:9px;color:#aab;padding:6px 6px}
  .chat-card .send{position:absolute;right:4px;bottom:6px;width:30px;height:30px;border-radius:50%;background:var(--pink);display:flex;align-items:center;justify-content:center}
  /* calendar */
  .calendar{position:absolute;left:725px;top:1397px;width:306px;height:165px;background:var(--white);border-radius:8px;border-left:5px solid var(--teal);border-bottom:7px solid var(--teal);box-shadow:0 6px 18px rgba(0,0,0,.06);font-family:"Lexend",sans-serif;overflow:hidden}
  .calendar .title{position:absolute;left:7px;top:5px;font-size:10px;font-weight:500}
  .calendar .month{position:absolute;left:40px;top:24px;width:145px;display:flex;justify-content:space-between;align-items:center;font-size:8px}
  .calendar .month i{width:17px;height:17px;border-radius:50%;background:#e6eefe;display:block}
  .calendar .grid{position:absolute;left:4px;top:50px;display:grid;grid-template-columns:repeat(7,30.6px);row-gap:6px;font-size:6px;text-align:center;color:var(--muted)}
  .calendar .grid b{width:22px;height:22px;line-height:22px;margin:0 auto;border-radius:50%;font-weight:500;font-size:7px}
  .calendar .grid .on{background:#e6eefe;color:var(--blue)}
  .calendar .grid .sel{background:var(--blue);color:var(--white)}
  .calendar .slots{position:absolute;left:218px;top:53px;display:flex;flex-direction:column;gap:7px}
  .calendar .slots span{width:80px;height:29px;border:1px solid #c9d9fb;border-radius:4px;font-size:8px;font-weight:500;color:var(--blue);display:flex;align-items:center;justify-content:center}
  /* lead table */
  .lead-table{position:absolute;left:222px;top:1752px;width:290px;height:160px;background:var(--white);border-left:7px solid var(--pink);border-bottom:7px solid var(--pink);border-radius:6px;box-shadow:0 6px 18px rgba(0,0,0,.06);font-family:"Lexend",sans-serif;overflow:hidden}
  .lead-table table{width:100%;border-collapse:collapse}
  .lead-table th{background:var(--blue);color:var(--white);font-size:8px;font-weight:700;text-align:left;padding:6px 10px;height:24px}
  .lead-table td{font-size:7.5px;line-height:11px;vertical-align:middle;padding:6px 4px;border-bottom:1px solid #e5e7ec;color:var(--ink)}
  .lead-table td + td{border-left:1px solid #e5e7ec;color:var(--muted);width:60px}
  .lead-table ul{padding-left:14px}
  /* cta */
  .cta-title{position:absolute;left:0;width:1200px;top:2297px;text-align:center;font-family:"Lexend",sans-serif;font-weight:400;font-size:72px;line-height:78px;color:var(--white);letter-spacing:-1px}
  .footer-line{position:absolute;left:197px;top:2950px;width:805px;height:1px;background:#e1e1e4}
  .legal{position:absolute;left:197px;top:2975px;font-size:11px;color:var(--ink)}
  .social-row{position:absolute;left:910px;top:2973px;display:flex;gap:8px}
  .social-row span{width:16px;height:16px;border-radius:50%;background:var(--blue)}
</style>
</head>
<body>

<svg class="backdrop" width="1200" height="3008" viewBox="0 0 1200 3008" aria-hidden="true">
  <path d="M0 0H1200V690Q1120 720 1040 700Q900 690 700 690Q450 690 260 712Q120 726 40 660Q0 620 0 560Z" fill="var(--mint)"/>
  <path d="M0 0H150Q150 150 40 180Q10 185 0 182Z" fill="var(--teal)"/>
  <ellipse cx="1120" cy="580" rx="110" ry="115" fill="var(--teal)"/>
  <path d="M990 5Q990 130 1100 138Q1180 140 1200 100" fill="none" stroke="var(--teal-line)" stroke-width="1"/>
  <path d="M0 395Q150 380 175 500Q190 610 50 650" fill="none" stroke="var(--teal-line)" stroke-width="1"/>
  <path d="M1200 860Q1080 880 1075 990Q1075 1080 1200 1090" fill="none" stroke="var(--teal-line)" stroke-width="1"/>
  <path d="M0 1300Q120 1290 125 1370Q125 1470 0 1555" fill="none" stroke="var(--teal-line)" stroke-width="1"/>
  <path d="M1200 1705Q1050 1720 1045 1830Q1045 1950 1200 1965" fill="none" stroke="var(--teal-line)" stroke-width="1"/>
  <circle cx="329" cy="1034" r="188" fill="var(--pink-soft)"/>
  <circle cx="881" cy="1411" r="188" fill="var(--mint)"/>
  <circle cx="329" cy="1880" r="188" fill="var(--pink-soft)"/>
  <g fill="none" stroke="#7a7a80" stroke-width="1.4" stroke-dasharray="6 6">
    <path d="M585 812Q560 850 480 838Q360 815 280 830Q220 850 205 900"/>
    <path d="M375 1183Q480 1220 575 1235"/>
    <path d="M628 1250Q720 1265 800 1280"/>
    <path d="M930 1600Q880 1690 760 1690Q680 1690 628 1670"/>
    <path d="M572 1660Q500 1620 400 1620Q260 1620 220 1720"/>
    <path d="M370 2042Q560 2090 590 2185"/>
  </g>
  <ellipse cx="1150" cy="2180" rx="110" ry="170" fill="var(--mint)"/>
  <path d="M0 2410Q120 2230 330 2190Q520 2160 700 2165Q900 2170 1060 2210Q1140 2230 1200 2270V2720Q1100 2700 980 2680Q800 2660 640 2665Q440 2675 280 2730Q140 2770 0 2760Z" fill="var(--teal)"/>
  <path d="M150 2235Q250 2270 240 2400" fill="none" stroke="var(--teal-line)" stroke-width="1" opacity=".6"/>
  <path d="M690 2640Q780 2560 960 2560" fill="none" stroke="var(--teal-line)" stroke-width="1" opacity=".6"/>
  <path d="M300 2710Q600 2650 900 2675" fill="none" stroke="var(--pink)" stroke-width="1" opacity=".5"/>
  <path d="M565 3000Q620 2920 720 2930Q820 2940 818 3008" fill="none" stroke="var(--teal-line)" stroke-width="1"/>
  <ellipse cx="891" cy="296" rx="150" ry="110" fill="var(--white)" stroke="#555" stroke-width="1" stroke-dasharray="4 4"/>
  <circle cx="791" cy="420" r="25" fill="var(--white)" stroke="#555" stroke-dasharray="3 3"/>
  <circle cx="782" cy="471" r="17" fill="var(--white)" stroke="#555" stroke-dasharray="3 3"/>
</svg>

<header>
  <div class="brand abs" style="left:197px;top:22px;font-size:50px;">pipwoof!</div>
  <div class="abs" style="left:807px;top:36px;width:37px;height:37px;border-radius:50%;background:#c8cffb;"></div>
  <a class="btn btn--blue" style="left:857px;top:36px;width:146px;height:37px;padding:0 12px 0 18px;">Register now
    <svg viewBox="0 0 14 14"><path d="M3 11L11 3M5 3H11V9" stroke="#fff" fill="none" stroke-width="1.2"/></svg></a>
</header>

<section class="hero">
  <h1 class="h-display abs" style="left:200px;top:178px;font-size:95px;"><span class="underlined">Welcome!</span></h1>
  <p class="bubble-text">Pip Talks To Your Leads, Qualifies Them, And Gets Them On Your Calendar.</p>
  <div class="illustration" role="img" aria-label="Smiling cartoon puppy mascot peeking over a board" style="left:450px;top:356px;width:300px;height:225px;"></div>
  <div class="abs" style="left:350px;top:566px;width:500px;height:134px;background:var(--white);border-top:3px solid #ddd;"></div>
  <a class="btn btn--pink" style="left:462px;top:617px;width:275px;height:36px;">See an example!
    <svg viewBox="0 0 14 14"><path d="M3 11L11 3M5 3H11V9" stroke="#fff" fill="none" stroke-width="1.2"/></svg></a>
  <a class="btn btn--teal" style="left:462px;top:666px;width:275px;height:36px;">Create your Pip now!
    <svg viewBox="0 0 14 14"><path d="M3 11L11 3M5 3H11V9" stroke="#fff" fill="none" stroke-width="1.2"/></svg></a>
</section>

<section class="feature">
  <div class="icon-dot icon-dot--pink" style="left:572px;top:760px;">
    <svg viewBox="0 0 26 26"><rect x="4" y="6" width="18" height="14" rx="2" fill="none" stroke="var(--pink)" stroke-width="2"/><path d="M7 11H19M7 15H15" stroke="var(--pink)" stroke-width="2"/></svg></div>
  <div class="chat-card">
    <div class="avatar"></div>
    <div class="name">Maren Hair</div>
    <div class="role">Hairdresser/Stylist</div>
    <div class="socials"><span></span><span></span><span></span><span></span></div>
    <div class="bot" role="img" aria-label="Puppy assistant avatar"></div>
    <div class="msg">Hi! I'm Pip, Maren's assistant.<br>How did you hear about Maren?</div>
    <div class="input">Enter your message.</div>
    <div class="send"><svg width="14" height="14" viewBox="0 0 14 14"><path d="M2 7L12 2L8 12L7 8Z" fill="none" stroke="#fff" stroke-width="1.3"/></svg></div>
  </div>
  <div class="illustration" role="img" aria-label="Puppy mascot holding a hairbrush and mirror" style="left:152px;top:1100px;width:110px;height:100px;"></div>
  <h2 class="h-display abs" style="left:591px;top:905px;font-size:72px;">Customize<br><span class="underlined">And Share</span></h2>
  <p class="body-copy abs" style="left:591px;top:1076px;width:375px;line-height:25px;">Pip Talks To Your Leads, Qualifies Them, And Gets Them On Your Calendar.</p>
</section>

<section class="feature">
  <div class="icon-dot icon-dot--mint" style="left:572px;top:1210px;">
    <svg viewBox="0 0 26 26"><circle cx="10" cy="8" r="4" fill="var(--teal)"/><path d="M3 21Q4 13 10 13Q14 13 15 16" fill="var(--teal)"/><circle cx="18" cy="18" r="5" fill="var(--teal)"/><path d="M15.5 18L17.5 20L20.5 16" stroke="#fff" fill="none" stroke-width="1.5"/></svg></div>
  <h2 class="h-display abs" style="left:200px;top:1322px;font-size:72px;">Qualify And<br><span class="underlined">Schedule</span></h2>
  <p class="body-copy abs" style="left:200px;top:1490px;width:375px;">Get The Information You Need From Your Customers. After They Meet Your Criteria, They Can Book A Meeting Directly On Your Calendar.</p>
  <div class="calendar">
    <div class="title">Select a Date &amp; Time</div>
    <div class="month"><i></i><span>June 2023</span><i></i></div>
    <div class="grid">
      <span>SUN</span><span>MON</span><span>TUE</span><span>WED</span><span>THU</span><span>FRI</span><span>SAT</span>
      <b></b><b></b><b></b><b></b><b class="on">1</b><b class="on">2</b><b>3</b>
      <b>4</b><b class="on">5</b><b class="on">6</b><b class="on">7</b><b class="on">8</b><b class="on">9</b><b>10</b>
      <b>11</b><b class="on">12</b><b class="sel">13</b><b class="on">14</b><b class="on">15</b><b class="on">16</b><b>17</b>
    </div>
    <div class="slots"><span>10:00am</span><span>10:30am</span><span>11:00am</span></div>
  </div>
  <div class="illustration" role="img" aria-label="Puppy mascot wearing glasses holding a clipboard" style="left:962px;top:1256px;width:100px;height:106px;"></div>
</section>

<section class="feature">
  <div class="icon-dot icon-dot--pink" style="left:572px;top:1638px;">
    <svg viewBox="0 0 26 26"><circle cx="13" cy="8" r="3.5" fill="var(--pink)"/><circle cx="6" cy="10" r="2.5" fill="var(--pink)"/><circle cx="20" cy="10" r="2.5" fill="var(--pink)"/><path d="M8 20Q8 13 13 13Q18 13 18 20Z M2 19Q2 14 6 14Q8 14 8.5 15 M24 19Q24 14 20 14Q18 14 17.5 15" fill="var(--pink)"/></svg></div>
  <div class="lead-table">
    <table>
      <tr><th>summary</th><th>email</th></tr>
      <tr><td><ul><li>Interested in a fitness coach</li><li>Does not currently work out</li><li>Specifically interested in arms and strength</li><li>In the Seattle area and flexible on time</li></ul></td><td>danreyes@</td></tr>
      <tr><td><ul><li>Interested in a new fitness coach</li><li>Works out 3 times a week</li><li>Has a fitness instructor now but his approach is too relaxed</li></ul></td><td>amyholton</td></tr>
    </table>
  </div>
  <div class="illustration" role="img" aria-label="Puppy mascot with a megaphone" style="left:152px;top:1944px;width:114px;height:106px;"></div>
  <h2 class="h-display abs" style="left:591px;top:1750px;font-size:72px;">Manage<br><span class="underlined">Your Leads</span></h2>
  <p class="body-copy abs" style="left:591px;top:1924px;width:375px;">Get Notified Via Email Or Text. See A Summary Of Each Lead And Manage Them In One Place. Search, Sort, Add Notes, And More.</p>
</section>

<section class="cta">
  <h2 class="cta-title">Let Pip Handle<br>Your Leads <span class="underlined underlined--pink">Today!</span></h2>
  <a class="btn btn--white" style="left:490px;top:2487px;width:219px;height:35px;">Create your Pip now!
    <svg viewBox="0 0 14 14"><path d="M3 11L11 3M5 3H11V9" stroke="#333" fill="none" stroke-width="1.2"/></svg></a>
  <div class="illustration" role="img" aria-label="Large happy puppy mascot" style="left:0;top:2450px;width:320px;height:338px;"></div>
  <div class="illustration" role="img" aria-label="Puppy mascot sitting" style="left:850px;top:2550px;width:262px;height:275px;"></div>
</section>

<footer>
  <div class="brand abs" style="left:0;width:1200px;text-align:center;top:2753px;font-size:54px;">pipwoof!</div>
  <div class="abs" style="left:485px;top:2845px;width:22px;height:22px;border-radius:50%;background:var(--blue);"></div>
  <div class="abs" style="left:522px;top:2848px;width:1px;height:18px;background:#ccc;"></div>
  <div class="abs" style="left:540px;top:2850px;font-size:11px;">Have Feedback? Let Us Know!</div>
  <div class="footer-line"></div>
  <div class="legal">© 2023 PipWoof.ai. All Rights Reserved. Terms Of Use</div>
  <div class="social-row"><span></span><span></span><span></span><span></span></div>
</footer>

</body>
</html>
```